Verpackungen  für Low-Carb Backwaren
Verpackungen für Low-Carb Backwaren
Zielgruppe
Wir erzeugen Low-Carb Backwaren, die Zielgruppe sind ernährungsbewusste Konsumenten
Aufgabenstellung
Die Verpackung wird eine durchsichtige Brötchenverpackung aus Kunststoff sein, das Design wird in Form eines Klebeetiketts auf der Verpackung angebracht. Der Inhalt sind 4 Stück Brötchen. Das Design muss modern sein und auffallen. Es muss Genuss und gesundes Essen beinhalten. Ich werde mit einem Foto von mir ebenfalls auf der Verpackung integriert. Es muss ein hoher Wiedererkennungswert entstehen. Bei den mitgelieferten beiden Produktbildern handelt es sich lediglich um Beispiele, die ich mit KI erzeugt habe um eine ungefähre Richtung vorzugeben. Diese beiden Bilder dienen nur zur groben Orientierung

```html
<!DOCTYPE html>
<html lang="en">
<head>
<meta charset="utf-8">
<title>Nuvela – Low Carb Rolls Label</title>
<link rel="stylesheet" href="https://fonts.googleapis.com/css2?family=Bebas+Neue&family=Fira+Sans+Condensed:wght@600&display=swap">
<style>
  :root {
    --backdrop: #ebe7df;
    --cream: #faf1e3;
    --cream-deep: #f3e6d2;
    --orange: #e0983f;
    --orange-light: #e8a95a;
    --brown: #4b2a20;
    --badge-ring: #8a5a44;
  }
  html, body {
    margin: 0;
    padding: 0;
    width: 1046px;
    height: 1200px;
    overflow: hidden;
    background: var(--backdrop);
  }
  .label {
    position: absolute;
    left: 171px;
    top: 60px;
    width: 703px;
    height: 1079px;
    border-radius: 16px;
    background: linear-gradient(160deg, var(--cream) 60%, var(--cream-deep));
    overflow: hidden;
  }
  .corner-band {
    position: absolute;
    left: 0;
    top: 0;
    width: 703px;
    height: 249px;
  }
  .brand-seal {
    position: absolute;
    left: 292px;
    top: 39px;
    width: 170px;
    height: 170px;
    border-radius: 50%;
    background: var(--cream);
    box-shadow: 0 0 0 6px var(--orange-light);
    display: flex;
    align-items: center;
    justify-content: center;
  }
  .brand-name {
    font-family: "Fira Sans Condensed", sans-serif;
    font-weight: 600;
    font-size: 44px;
    color: var(--brown);
  }
  .cookie-art {
    position: absolute;
    left: 44px;
    top: 85px;
    width: 288px;
    height: 282px;
    border-radius: 50%;
    background: radial-gradient(circle at 45% 45%, var(--orange) 55%, var(--brown) 72%);
  }
  .headline {
    position: absolute;
    margin: 0;
    font-family: "Bebas Neue", sans-serif;
    font-weight: 400;
    color: var(--brown);
    line-height: 1;
  }
  .headline-snack { left: 71px; top: 412px; font-size: 76px; }
  .headline-stay  { left: 76px; top: 497px; font-size: 118px; }
  .headline-young { left: 119px; top: 616px; font-size: 122px; }
  .founder-photo {
    position: absolute;
    left: 407px;
    top: 282px;
    width: 293px;
    height: 644px;
    border-radius: 40px;
    background: linear-gradient(180deg, #e8c9b5 0%, #f0c8d6 35%, #4b6fa0 70%, #e9e6e2 100%);
  }
  .benefits {
    position: absolute;
    left: 110px;
    top: 752px;
    margin: 0;
    padding: 0;
    list-style: none;
    font-family: "Fira Sans Condensed", sans-serif;
    font-weight: 600;
    font-size: 38px;
    color: var(--orange);
  }
  .benefits li {
    height: 54px;
    display: flex;
    align-items: center;
  }
  .benefits li::before {
    content: "";
    width: 13px;
    height: 13px;
    border-radius: 50%;
    background: var(--orange);
    margin-right: 17px;
  }
  .badges {
    position: absolute;
    left: 99px;
    top: 932px;
    display: flex;
    gap: 35px;
  }
  .badge {
    width: 98px;
    height: 98px;
    border-radius: 50%;
    background: #fff;
    box-shadow: inset 0 0 0 4px var(--badge-ring), 0 2px 6px rgba(75, 42, 32, 0.2);
  }
</style>
</head>
<body>
  <main class="label">
    <svg class="corner-band" viewBox="0 0 703 249" aria-hidden="true">
      <path fill="#e0983f" d="M300 0 H703 V215 C680 210 665 222 660 235 C640 215 605 225 600 245 C590 215 545 205 525 225 C510 180 460 165 430 175 C420 140 380 120 340 120 C325 80 310 30 300 0 Z"/>
    </svg>

    <div class="brand-seal"><span class="brand-name">Nuvela</span></div>

    <div class="cookie-art" role="img" aria-label="Illustration of a bitten cookie with crumbs and the hand-lettered words Healthy &amp; tasty"></div>

    <h1 class="headline headline-snack">Snack smart.</h1>
    <p class="headline headline-stay">Stay</p>
    <p class="headline headline-young">Young.</p>

    <div class="founder-photo" role="img" aria-label="Photo of the smiling founder in a pink shirt and jeans, jumping with both thumbs up"></div>

    <ul class="benefits">
      <li>Hich protein</li>
      <li>Low carb</li>
      <li>High fibre</li>
    </ul>

    <div class="badges">
      <div class="badge" role="img" aria-label="Vegan badge"></div>
      <div class="badge" role="img" aria-label="Healthily sugared badge"></div>
      <div class="badge" role="img" aria-label="Gluten free badge"></div>
      <div class="badge" role="img" aria-label="Keto badge"></div>
    </div>
  </main>
</body>
</html>
```